Veltrium stationery design

Design stationery for us that fits with the colours of the logo. We are looking for letterheads, business cards etc. Something we can use for a prospectus and marketing presentations in power point. Must be completed in such a manner that it represents a corporate image for large enterprise clients and other large organisations. The company is a project assurance and monitoring company that works in all industries.

```html
<!DOCTYPE html>
<html lang="en">
<head>
<meta charset="utf-8">
<title>Veltrium Stationery</title>
<link rel="stylesheet" href="https://fonts.googleapis.com/css2?family=Montserrat:wght@400;500;700&family=Arimo:wght@400&display=swap">
<style>
  :root {
    --bg: #ececec;
    --paper: #f7f7f7;
    --blue: #1f5a96;
    --blue-deep: #2e3d6e;
    --orange: #e8572a;
    --ink: #333a44;
    --grey: #555b63;
  }
  * { box-sizing: border-box; margin: 0; padding: 0; }
  html, body { width: 1200px; height: 795px; overflow: hidden; }
  body { background: var(--bg); position: relative; font-family: "Montserrat", sans-serif; color: var(--ink); }

  .sheet { position: absolute; background: var(--paper); box-shadow: 0 1px 3px rgba(0,0,0,.12); }
  .brand-blue { background: linear-gradient(180deg, var(--blue) 0%, var(--blue-deep) 100%); }

  .wordmark { position: absolute; display: flex; align-items: center; font-family: "Montserrat", sans-serif; font-weight: 700; letter-spacing: .02em; white-space: nowrap; }
  .wordmark .dot { border-radius: 50%; background: var(--orange); flex: none; }
  .wordmark.on-light { color: var(--blue); }
  .wordmark.on-dark { color: #ffffff; }

  /* Letterhead */
  .letterhead { left: 292px; top: 99px; width: 293px; height: 414px; }
  .letterhead .wordmark { left: 36px; top: 30px; font-size: 13px; gap: 5px; }
  .letterhead .wordmark .dot { width: 11px; height: 11px; }
  .contact-block { position: absolute; left: 197px; top: 25px; font-size: 5.4px; line-height: 1.3; color: var(--grey); }
  .contact-block .row { display: flex; align-items: center; gap: 2px; }
  .icon { width: 4.5px; height: 4.5px; flex: none; fill: var(--orange); }
  .letter { position: absolute; left: 35px; width: 222px; font-family: "Arimo", sans-serif; font-size: 4.6px; line-height: 1.38; color: #2b2b2b; }
  .letter.addressee { top: 105px; }
  .letter.body { top: 162px; text-align: justify; }
  .letter.body p { margin-bottom: 5px; }
  .letter.sign-off { top: 317px; }

  /* Folder */
  .folder { left: 637px; top: 80px; width: 346px; height: 437px; }
  .folder .spine { position: absolute; left: 3px; top: 0; bottom: 0; width: 16px; border-left: 1px solid rgba(255,255,255,.08); border-right: 1px solid rgba(0,0,0,.12); }
  .folder .wordmark { left: 50%; top: 206px; transform: translateX(-50%); font-size: 21px; gap: 8px; }
  .folder .wordmark .dot { width: 18px; height: 18px; }
  .web { position: absolute; left: 0; right: 0; text-align: center; color: #fff; font-weight: 400; }
  .web .accent { color: var(--orange); }
  .folder .web { top: 384px; font-size: 10px; letter-spacing: 2.2px; }

  /* Business cards */
  .card { left: 187px; width: 132px; height: 75px; }
  .card.front { top: 551px; }
  .card.front .wordmark { left: 50%; top: 30px; transform: translateX(-50%); font-size: 10px; gap: 4px; }
  .card.front .wordmark .dot { width: 8px; height: 8px; }
  .card.front .web { top: 61px; font-size: 4px; letter-spacing: .8px; }
  .card.back { top: 646px; }
  .card.back .wordmark { right: 12px; top: 12px; font-size: 7.5px; gap: 3px; }
  .card.back .wordmark .dot { width: 6px; height: 6px; }
  .card-person { position: absolute; left: 12px; right: 12px; top: 38px; }
  .card-person .name { font-size: 5px; font-weight: 700; color: var(--blue-deep); }
  .card-person .role { display: flex; align-items: center; gap: 2px; font-size: 4px; color: var(--orange); }
  .card-person .role::after { content: ""; flex: 1; height: .5px; background: var(--orange); }
  .card-details { position: absolute; left: 12px; right: 12px; top: 53px; display: flex; justify-content: space-between; font-size: 3.6px; line-height: 1.25; color: var(--grey); }
  .card-details .row { display: flex; align-items: center; gap: 1.5px; }
  .card-details .icon { width: 3.2px; height: 3.2px; }
  .card-details .address { text-align: right; }

  /* Envelopes */
  .envelope-front { left: 353px; top: 561px; width: 329px; height: 157px; }
  .envelope-front .wordmark { left: 27px; top: 22px; font-size: 11px; gap: 4px; }
  .envelope-front .wordmark .dot { width: 9px; height: 9px; }
  .envelope-front .return-address { position: absolute; left: 26px; top: 121px; font-size: 7.4px; line-height: 1.15; color: var(--grey); }
  .envelope-back { left: 714px; top: 561px; width: 328px; height: 156px; }
  .envelope-back .flap { position: absolute; left: 0; top: 0; width: 100%; height: 56px; }
  .envelope-back .wordmark { left: 50%; top: 21px; transform: translateX(-50%); font-size: 10.5px; gap: 4px; }
  .envelope-back .wordmark .dot { width: 9px; height: 9px; }
</style>
</head>
<body>

<svg width="0" height="0" style="position:absolute" aria-hidden="true">
  <symbol id="i-phone" viewBox="0 0 10 10"><path d="M2 1h2l1 2.5-1.2.8a6 6 0 0 0 2 2L6.6 5 9 6v2c0 .6-.4 1-1 1A8 8 0 0 1 1 2c0-.6.4-1 1-1z"/></symbol>
  <symbol id="i-mail" viewBox="0 0 10 10"><path d="M0 2h10v6H0z M0 2l5 3.5L10 2" /></symbol>
  <symbol id="i-web" viewBox="0 0 10 10"><circle cx="5" cy="5" r="4.5"/></symbol>
</svg>

<!-- Letterhead -->
<section class="sheet letterhead">
  <div class="wordmark on-light"><span class="dot"></span>VELTRIUM</div>
  <div class="contact-block">
    <div>250 Harbor Lane</div>
    <div>Suite 310 Austin 482</div>
    <div class="row"><svg class="icon"><use href="#i-phone"/></svg>512-555-0187</div>
    <div class="row"><svg class="icon"><use href="#i-mail"/></svg>info@veltrium.com</div>
    <div class="row"><svg class="icon"><use href="#i-web"/></svg>www.veltrium.com</div>
  </div>
  <div class="letter addressee">
    First Name Last Name<br>Addressee's name<br>Building number/name and street<br>Post Town, Post Code
  </div>
  <div class="letter body">
    <p>Dear First Name</p>
    <p>Thank you for the opportunity to support your programme. Our assurance team reviews schedules, budgets and risks at every stage, giving your board a clear and independent view of progress. We work alongside your project leads to test controls, track delivery milestones and report early warnings before they become costly problems. Each review closes with practical actions, agreed owners and firm dates.</p>
    <p>We would welcome a short meeting to outline our monitoring approach and discuss how it could fit your current portfolio. Please contact our office at any time to arrange a convenient date.</p>
    <p>Sincerely,</p>
  </div>
  <div class="letter sign-off">First Name Last Name<br>Position</div>
</section>

<!-- Presentation folder -->
<section class="sheet folder brand-blue">
  <div class="spine"></div>
  <div class="wordmark on-dark"><span class="dot"></span>VELTRIUM</div>
  <div class="web">www.<span class="accent">veltrium</span>.com</div>
</section>

<!-- Business card front -->
<section class="sheet card front brand-blue">
  <div class="wordmark on-dark"><span class="dot"></span>VELTRIUM</div>
  <div class="web">www.<span class="accent">veltrium</span>.com</div>
</section>

<!-- Business card back -->
<section class="sheet card back">
  <div class="wordmark on-light"><span class="dot"></span>VELTRIUM</div>
  <div class="card-person">
    <div class="name">DANA WHITFIELD</div>
    <div class="role">Director</div>
  </div>
  <div class="card-details">
    <div>
      <div class="row"><svg class="icon"><use href="#i-phone"/></svg>512-555-0187</div>
      <div class="row"><svg class="icon"><use href="#i-mail"/></svg>info@veltrium.com</div>
      <div class="row"><svg class="icon"><use href="#i-web"/></svg>www.veltrium.com</div>
    </div>
    <div class="address">2500 Harbor Lane<br>Suite 310 Austin,<br>Texas 78701</div>
  </div>
</section>

<!-- Envelope front -->
<section class="sheet envelope-front">
  <div class="wordmark on-light"><span class="dot"></span>VELTRIUM</div>
  <div class="return-address">250 Harbor Lane<br>Suite 310 Austin 482</div>
</section>

<!-- Envelope back -->
<section class="sheet envelope-back">
  <svg class="flap" viewBox="0 0 328 56" preserveAspectRatio="none" aria-hidden="true">
    <defs>
      <linearGradient id="flap-fill" x1="0" y1="0" x2="0" y2="1">
        <stop offset="0" stop-color="var(--blue)"/>
        <stop offset="1" stop-color="#24508a"/>
      </linearGradient>
    </defs>
    <path d="M0 0H328L322 48Q321 55 314 55H14Q7 55 6 48Z" fill="url(#flap-fill)"/>
  </svg>
  <div class="wordmark on-dark"><span class="dot"></span>VELTRIUM</div>
</section>

</body>
</html>
```